NEW Escape Room. Fun, Dark and Mysterious.

Escape Room Website. Bookings and scheduling of appointments will be organised with Bookvane through the site. Most appointments will be created online through the booking system with some payments coming through in person by drop-ins. Groups will be from 2 - 8 people with a sliding scale of prices. We will start with one game playable and one saying coming soon. We will also eventually have 4 games up and running at once so will need it to be able to expand. We don't have any images of the rooms because it all relies heavily on mystery. Appointments are each 1 hour long with 30 minutes in between.

Target Market(s)

15-35 year olds

Coding

Coded - Design and coding required

Number of Pages Required

5+ page

Font styles to use
Decorative

Colors

Designer to choose colors to be used in the design.

Requirements
Must have
• Graphics showing what an escape room is.
• Page for About - What is an escape room
• Page for Games - Showing each of the different games which can be played with links to booking page. We have one game to start - the surgeons shadows. A victorian doctors office and serial killers. Then a game coming soon which is aztec/mayan/jungle/harold Crane feel.
• FAQ Page
Nice to have
• Graphics for multiple players ie 2 players, 3 players, 4 players etc
• Dark and Mysterious feel.
• Inspiration from Puzzle Vault, Cipher Lodge, Quest Lockbox
Should not have
• Cartoony/childish. Pink.
• Not bloody or dripping letters etc - not cliche.
• Not horror themed.

```html
<!DOCTYPE html>
<html lang="en">
<head>
<meta charset="utf-8">
<title>FAQ</title>
<link rel="stylesheet" href="https://fonts.googleapis.com/css2?family=Cinzel+Decorative:wght@700&family=Cinzel:wght@700&family=Cabin+Condensed:wght@400&display=swap">
<style>
  :root {
    --night: #000000;
    --nav-red: #3d0004;
    --nav-rule: #6b6b6b;
    --panel: rgba(40, 0, 3, 0.72);
    --ground: #5e1a1d;
    --ground-deep: #3a0207;
    --ink: #ffffff;
    --text: #f2eaea;
  }
  * { margin: 0; padding: 0; box-sizing: border-box; }
  html, body { width: 1200px; height: 700px; overflow: hidden; background: var(--night); }
  .canvas { position: relative; width: 1200px; height: 700px; background: var(--night); overflow: hidden; }

  .site-nav {
    position: absolute; left: 0; top: 19px; width: 1200px; height: 44px;
    background: var(--nav-red); border-bottom: 1px solid var(--nav-rule);
  }
  .site-nav a {
    position: absolute; top: 50%; transform: translate(-50%, -50%);
    font-family: "Cinzel Decorative", serif; font-weight: 700; font-size: 21px; color: var(--ink);
    text-decoration: none; white-space: nowrap; letter-spacing: 0.5px;
  }

  .graveyard {
    position: absolute; left: 0; top: 560px; width: 1200px; height: 140px;
    background: linear-gradient(180deg, var(--ground) 0%, var(--ground) 69%, var(--ground-deep) 69%, var(--ground-deep) 100%);
    border-radius: 40% 40% 0 0 / 8% 8% 0 0;
  }

  .page-title {
    position: absolute; left: 610px; top: 90px; transform: translateX(-50%);
    text-align: center; color: var(--ink);
  }
  .page-title h1 {
    font-family: "Cinzel Decorative", serif; font-weight: 700;
    font-size: 52px; line-height: 1; letter-spacing: 1px;
  }
  .page-title p {
    font-family: "Cinzel", serif; font-weight: 700;
    font-size: 9px; margin-top: 12px; white-space: nowrap; letter-spacing: 0.2px;
  }

  .faq-panel {
    position: absolute; top: 134px; width: 456px; height: 461px;
    background: var(--panel);
    font-family: "Cabin Condensed", sans-serif; font-size: 14.3px; color: var(--text);
    line-height: 21.3px; white-space: nowrap;
  }
  .faq-panel.left { left: 69px; }
  .faq-panel.right { left: 696px; }
  .faq-list { position: absolute; left: 12px; top: 25px; }
  .faq-panel.right .faq-list { left: 17px; }
  .question { text-transform: uppercase; }
  .answer { padding-left: 42px; }

  .price-table { border-collapse: collapse; margin: 11px 0 9px 64px; }
  .price-table th { font-weight: 400; text-align: left; padding: 0; height: 21.3px; }
  .price-table .head-person { display: inline-block; margin-left: 42px; width: 124px; }
  .price-table td { padding: 0; height: 21.3px; }
  .price-table .group-size { width: 89px; }
  .price-table .cur { width: 12px; }
  .price-table .amt { text-align: right; }
  .price-table .pp { width: 55px; }
  .price-table .gap { width: 17px; }
  .price-table .pg { width: 54px; }
</style>
</head>
<body>
<div class="canvas">
  <nav class="site-nav">
    <a href="#" style="left:137px">HOME PAGE</a>
    <a href="#" style="left:332px">ABOUT</a>
    <a href="#" style="left:503px">GAMES</a>
    <a href="#" style="left:720px">CONTACT US</a>
    <a href="#" style="left:883px">FAQ</a>
    <a href="#" style="left:1048px">BOOK NOW</a>
  </nav>

  <div class="graveyard" role="img" aria-label="Dark red graveyard silhouette with tombstones, crosses, grass and an iron fence"></div>

  <header class="page-title">
    <h1>FAQ</h1>
    <p>FREQUENTLY ASKED QUESTIONS</p>
  </header>

  <section class="faq-panel left">
    <div class="faq-list">
      <p class="question">Can I buy a voucher for an escape room?</p>
      <p class="answer">- Yes!&nbsp;&nbsp; Give us a call so that we can organise a voucher.</p>
      <p class="question">What does it cost?</p>
      <p class="answer">- The prices are based per person, the more people in the room,<br>the cheaper it is per person!</p>
      <table class="price-table">
        <tr><th colspan="6"><span class="head-person">Price Per Person</span>Price Per Group</th></tr>
        <tr><td class="group-size">2 People</td><td class="cur">$</td><td class="amt pp">42.00</td><td class="gap"></td><td class="cur">$</td><td class="amt pg">84.00</td></tr>
        <tr><td class="group-size">3 People</td><td class="cur">$</td><td class="amt pp">40.00</td><td class="gap"></td><td class="cur">$</td><td class="amt pg">120.00</td></tr>
        <tr><td class="group-size">4 People</td><td class="cur">$</td><td class="amt pp">38.00</td><td class="gap"></td><td class="cur">$</td><td class="amt pg">152.00</td></tr>
        <tr><td class="group-size">5 People</td><td class="cur">$</td><td class="amt pp">37.00</td><td class="gap"></td><td class="cur">$</td><td class="amt pg">185.00</td></tr>
        <tr><td class="group-size">6 People</td><td class="cur">$</td><td class="amt pp">36.00</td><td class="gap"></td><td class="cur">$</td><td class="amt pg">216.00</td></tr>
        <tr><td class="group-size">7 or More</td><td class="cur">$</td><td class="amt pp">35.00</td><td class="gap"></td><td class="cur">$</td><td class="amt pg">245.00</td></tr>
      </table>
      <p class="question">How can I cancel my booking?</p>
      <p class="answer">Bookings are non refundable.&nbsp; If you must cancel your booking, please give<br>us a call as soon as possible and we can try to reschedule your appointment.</p>
      <p class="question">I need to change my booking!</p>
      <p class="answer">We need as much notice as possible as we don’t want anyone to miss out on<br>a slot. Give us a call and we will do our best to accommodate a different<br>time!&nbsp; If the slot is available, then no problem!</p>
    </div>
  </section>

  <section class="faq-panel right">
    <div class="faq-list">
      <p class="question">How long does the game take?</p>
      <p class="answer">-The game itself is 60 minutes, however you should allow 90 minutes<br>to go through waivers, story, take pictures, high five your friends or wallow<br>in self pity at your failure</p>
      <p class="question">What if we get stuck?</p>
      <p class="answer">-Don’t worry!&nbsp; We are here to help you.&nbsp; We will give you a walkie talkie<br>before you enter the room and you can ask us questions at any time!<br>Some rooms give you a limit of clues that you can ask for, but feel free to<br>talk to us as much as possible!&nbsp; If we see that you are spending too much<br>time on the wrong path, we might throw you a nudge too :)</p>
      <p class="question">How old do I have to be to play?</p>
      <p class="answer">-This seasons room is relatively dark.&nbsp; It has disturbing themes and images<br>inside the room, however it is all in good fun!&nbsp; We recommend children<br>are at the very least over 12.&nbsp; We have had 10 year olds go through alone<br>and put their elders to shame!&nbsp; Any children under the age of 16 not<br>accompanied by an adult will need parental permissions to play.&nbsp; If you<br>have any concerns, just contact the team and we can give some more<br>information.</p>
    </div>
  </section>
</div>
</body>
</html>
```